Can Design for Fun, Growing Health Food Brand

We are launching a brand new product, electrolyte seltzer drinks. We want the design to be clean/simple and slightly modern while staying true to our brand identity. Must say "Mineral Hydration" as the product descriptor, sub headline is "Carbonated electrolyte beverage with sea moss and real fruit juice". First flavors will be Watermelon Mint and Mango.

Target Market(s)

Women ages 30-50 who are interested in health wellness/trends

Industry/Entity Type

Health & Wellness

Font styles to use
Sans Serif

Requirements
Must have
• Tall, skinny can, current Bright Kelp Co Logo, use aluminum on can as element in design.
Nice to have
• Be fun, clean and modern. Would like to see the label less busy than our gels.
Should not have
• Avoid putting flavor on bottom 1/5 of can. No gradient color changes. Do not want really detailed or realistic fruit image, prefer drawings or similar.

```html
<!DOCTYPE html>
<html lang="en">
<head>
<meta charset="utf-8">
<title>Bright Kelp Co – Mineral Hydration Cans</title>
<link rel="stylesheet" href="https://fonts.googleapis.com/css2?family=Fira+Sans:wght@300;400;600&display=swap">
<style>
  :root {
    --backdrop: #f3eee9;
    --aluminum: #d7d8d9;
    --aluminum-light: #e6e7e8;
    --teal: #2f6b63;
    --watermelon: #d9475f;
    --watermelon-soft: #f2c6cd;
    --mango: #e98a2a;
    --mango-soft: #f7d9b8;
  }
  * { margin: 0; padding: 0; box-sizing: border-box; }
  html, body { width: 1200px; height: 1200px; overflow: hidden; }
  body {
    background: var(--backdrop);
    font-family: "Fira Sans", sans-serif;
    color: var(--teal);
    position: relative;
  }
  .can-label {
    position: absolute;
    top: 121px;
    width: 370px;
    height: 907px;
    background: linear-gradient(90deg, var(--aluminum) 0%, var(--aluminum-light) 45%, var(--aluminum) 100%);
    border-radius: 6px;
    overflow: hidden;
  }
  .can-label--watermelon { left: 168px; }
  .can-label--mango { left: 632px; }

  .brand {
    position: absolute;
    top: 114px;
    left: 34px;
    display: flex;
    align-items: center;
    gap: 12px;
  }
  .brand__dot {
    width: 68px; height: 68px;
    border: 3px solid var(--teal);
    border-radius: 50%;
    flex: none;
  }
  .brand__name {
    font-weight: 400;
    font-size: 28px;
    letter-spacing: 0.3px;
    color: var(--teal);
    white-space: nowrap;
  }

  .descriptor {
    position: absolute;
    left: 80px;
    top: 543px;
    transform: translate(-50%, -50%) rotate(-90deg);
    font-weight: 300;
    font-size: 60px;
    line-height: 1;
    letter-spacing: 1px;
    white-space: nowrap;
    color: var(--teal);
  }

  .flavor {
    position: absolute;
    left: 154px;
    top: 286px;
    font-weight: 600;
    font-size: 24px;
    line-height: 1.3;
    letter-spacing: 0.6px;
  }
  .can-label--mango .flavor { top: 314px; }
  .can-label--watermelon .flavor { color: var(--watermelon); }
  .can-label--mango .flavor { color: var(--mango); }

  .rule {
    position: absolute;
    left: 154px;
    top: 371px;
    width: 137px;
    height: 1px;
  }
  .can-label--watermelon .rule { background: var(--teal); }
  .can-label--mango .rule { background: var(--mango); }

  .subhead {
    position: absolute;
    left: 154px;
    top: 391px;
    font-size: 14px;
    line-height: 20px;
    font-weight: 400;
    white-space: nowrap;
  }

  .illustration {
    position: absolute;
    left: 149px;
    top: 511px;
    width: 180px;
    height: 177px;
    border-radius: 50%;
  }
  .can-label--watermelon .illustration { background: var(--watermelon-soft); }
  .can-label--mango .illustration { background: var(--mango-soft); }

  .facts {
    position: absolute;
    left: 155px;
    top: 704px;
    font-size: 11px;
    line-height: 17px;
    letter-spacing: 0.5px;
    text-transform: uppercase;
  }
  .facts__number { font-size: 15px; line-height: 19px; }
  .facts__dash { display: block; width: 9px; height: 1px; background: var(--teal); margin: 8px 0; }

  .volume {
    position: absolute;
    left: 155px;
    top: 872px;
    font-size: 13px;
    line-height: 16px;
    letter-spacing: 0.5px;
  }
</style>
</head>
<body>

<section class="can-label can-label--watermelon">
  <div class="brand"><span class="brand__dot"></span><span class="brand__name">BRIGHT KELP CO</span></div>
  <div class="descriptor">MINERAL HYDRATION</div>
  <h2 class="flavor">WATERMELON<br>MINT</h2>
  <div class="rule"></div>
  <p class="subhead">Carbonated<br>electrolyte<br>beverage with<br>sea moss and<br>real fruit juice</p>
  <div class="illustration" role="img" aria-label="Line drawing of a watermelon slice with mint leaves"></div>
  <div class="facts">
    <div class="facts__number">10</div>
    <div>Calories</div>
    <span class="facts__dash"></span>
    <div>No added<br>sugar</div>
    <span class="facts__dash"></span>
    <div>Plant<br>based</div>
  </div>
  <div class="volume">12 FL OZ (355 ML)</div>
</section>

<section class="can-label can-label--mango">
  <div class="brand"><span class="brand__dot"></span><span class="brand__name">BRIGHT KELP CO</span></div>
  <div class="descriptor">MINERAL HYDRATION</div>
  <h2 class="flavor">MANGO</h2>
  <div class="rule"></div>
  <p class="subhead">Carbonated<br>electrolyte<br>beverage with<br>sea moss and<br>real fruit juice</p>
  <div class="illustration" role="img" aria-label="Line drawing of a mango with a leafy sprig"></div>
  <div class="facts">
    <div class="facts__number">10</div>
    <div>Calories</div>
    <span class="facts__dash"></span>
    <div>No added<br>sugar</div>
    <span class="facts__dash"></span>
    <div>Plant<br>based</div>
  </div>
  <div class="volume">12 FL OZ (355 ML)</div>
</section>

</body>
</html>
```